Startup online payment business - Sporting / Golf, Swift Tee payment

Background:
Our business name is "Swift Tee" we provide online payments for golfing services via our website. We currently have a logo used on our website. No other design style has been developed. Our aim is to remove cash payments for service at golf clubs.

Our Key Values:
Quick and easy
Formal and polite
Fun with professional boundary
Mate-ship relationships
100% online digital

What we want from you:
Marketing design to be used on posters and stickers in a retail setting to direct customers to our online payment Chanel.
Design must incorporate attached logo, URL swifttee.com.au and our key values can act as a guide the type of design. We have used color Hex#007672 for logo background. We are open to use other colors.

Target Market(s)

Golf clubs and golf players

Industry/Entity Type

Golf Course

Font styles to use
Sans Serif

Requirements
Must have
• Directions to online payment via URL: swifttee.com.au
Nice to have
• We like the idea of the slogan: No Cash - No worries. Have attached home screen that will be available from URL link. Consideration if using mobile phone in image. Push the online payment and steps 1. Visit swifttee.com 2. Select club 3. Confirm payment
Should not have
• Cartoons

```html
<!DOCTYPE html>
<html lang="en">
<head>
<meta charset="utf-8">
<title>Swift Tee – No Cash, No Worries</title>
<link rel="stylesheet" href="https://fonts.googleapis.com/css2?family=Montserrat:ital,wght@0,400;0,500;0,600;1,300;1,400&family=Open+Sans:wght@400;600;800&display=swap">
<style>
  :root{
    --teal:#007672;
    --bright-green:#12c012;
    --panel:rgba(12,14,10,.62);
    --header:rgba(40,40,40,.82);
    --white:#ffffff;
    --phone-body:#f2f3f3;
    --phone-edge:#c9cdcf;
    --button-grey:#4a5058;
  }
  *{margin:0;padding:0;box-sizing:border-box}
  html,body{width:776px;height:1200px;overflow:hidden;background:#222}
  .poster{position:relative;width:776px;height:1200px;overflow:hidden;font-family:"Montserrat",sans-serif;color:var(--white)}
  .scene-photo{position:absolute;inset:0;
    background:
      linear-gradient(180deg,#34463a 0%,#5b6a55 14%,#b07a5c 26%,#8a8a78 36%,#4f6a3e 52%,#3f6a2a 70%,#3d6a26 100%)}
  .shapes{position:absolute;inset:0}
  .header{position:absolute;left:12px;top:0;width:752px;height:149px;background:var(--header);text-align:center}
  .header::before,.header::after{content:"";position:absolute;left:26px;right:26px;height:2px;background:var(--white)}
  .header::before{top:11px}
  .header::after{top:134px;left:96px;right:96px}
  .slogan{font-family:"Open Sans",sans-serif;font-weight:800;font-size:69px;line-height:1;color:var(--bright-green);padding-top:16px;letter-spacing:.5px;white-space:nowrap}
  .tagline{font-family:"Open Sans",sans-serif;font-size:31px;margin-top:8px}
  .tagline .brand{color:var(--teal);font-weight:600}
  .values{position:absolute;right:16px;font-family:"Montserrat",sans-serif;font-style:italic;font-weight:300;font-size:28px;letter-spacing:2px;text-align:right}
  .values.fast{top:166px}
  .values.convenient{top:213px}
  .values.trustworthy{top:257px;right:14px}
  .steps-panel{position:absolute;left:20px;top:162px;width:454px;height:581px;background:var(--panel)}
  .steps-title{position:absolute;left:48px;top:222px;font-weight:500;font-size:38px;letter-spacing:.5px}
  .steps-sub{position:absolute;left:72px;top:273px;font-style:italic;font-size:33px;letter-spacing:.5px}
  .big-three{position:absolute;left:156px;top:340px;font-weight:400;font-size:118px;line-height:1}
  .easy-steps{position:absolute;left:236px;top:360px;font-size:37px;line-height:45px}
  .step{position:absolute;left:61px;font-size:30px;display:flex;align-items:center;gap:24px}
  .step.one{top:500px}
  .step.two{top:577px;left:64px}
  .step.three{top:655px;left:64px}
  .step svg{flex:none}
  .brand-name{position:absolute;left:0;width:526px;top:968px;text-align:center;font-family:"Montserrat",sans-serif;font-weight:600;font-size:74px;letter-spacing:2px}
  .url{position:absolute;left:0;width:534px;top:1150px;text-align:center;font-size:25px;letter-spacing:1.6px}
</style>
</head>
<body>
<main class="poster">
  <div class="scene-photo" role="img" aria-label="Golfer swinging on a misty green fairway at sunrise, framed by tall gum trees"></div>

  <svg class="shapes" width="776" height="1200" viewBox="0 0 776 1200" aria-hidden="true">
    <polygon class="lower-band" points="0,976 776,780 776,1200 0,1200" fill="#007672"/>
    <polygon class="pointer" points="21,755 474,755 474,802 247,852 21,802" fill="#12c012"/>
    <polygon class="ribbon" points="662,163 776,163 776,205 662,205 690,184" fill="#007672"/>
    <polygon class="ribbon" points="549,210 776,210 776,252 549,252 584,231" fill="#007672"/>
    <polygon class="ribbon" points="541,255 776,255 776,298 541,298 570,276" fill="#007672"/>
  </svg>

  <header class="header">
    <h1 class="slogan">No Cash - No Worries</h1>
    <p class="tagline">Use <span class="brand">Swift Tee</span> to easily pay online.</p>
  </header>

  <p class="values fast">Fast</p>
  <p class="values convenient">Convenient</p>
  <p class="values trustworthy">Trustworthy</p>

  <section class="steps-panel" aria-label="Steps"></section>
  <h2 class="steps-title">GET ON THE GREEN</h2>
  <p class="steps-sub">without your green in</p>
  <p class="big-three">3</p>
  <p class="easy-steps">EASY<br>STEPS</p>

  <p class="step one">1. Visit swifttee.com
    <svg width="40" height="34" viewBox="0 0 40 34"><rect x="2" y="2" width="36" height="22" fill="none" stroke="#fff" stroke-width="3"/><rect x="15" y="24" width="10" height="6" fill="#fff"/><rect x="9" y="29" width="22" height="3" fill="#fff"/></svg>
  </p>
  <p class="step two">2. Select your club
    <svg width="38" height="44" viewBox="0 0 38 44"><path d="M10 36V3l22 11-22 9" fill="none" stroke="#fff" stroke-width="2.5"/><ellipse cx="17" cy="38" rx="15" ry="4" fill="none" stroke="#fff" stroke-width="2.5"/></svg>
  </p>
  <p class="step three">3. Confirm payment
    <svg width="38" height="38" viewBox="0 0 38 38"><circle cx="19" cy="19" r="16" fill="none" stroke="#fff" stroke-width="3"/><path d="M11 19l6 6 11-12" fill="none" stroke="#fff" stroke-width="3.5"/></svg>
  </p>

  <p class="brand-name">Swift Tee</p>
  <p class="url">www.swifttee.com.au</p>

  <svg class="shapes phone" width="776" height="1200" viewBox="0 0 776 1200" font-family="Open Sans, sans-serif">
    <rect x="520" y="717" width="211" height="438" rx="30" fill="var(--phone-body)" stroke="var(--phone-edge)" stroke-width="2"/>
    <circle cx="626" cy="732" r="2" fill="#333"/>
    <circle cx="592" cy="745" r="3" fill="#444"/>
    <rect x="607" y="743" width="38" height="3" rx="1.5" fill="#555"/>
    <circle cx="625" cy="1127" r="14" fill="none" stroke="#555" stroke-width="1.5"/>
    <rect x="532" y="771" width="188" height="332" fill="var(--teal)"/>
    <rect x="538" y="781" width="25" height="14" rx="3" fill="none" stroke="#fff" stroke-width=".8"/>
    <text x="550.5" y="791" font-size="6" fill="#fff" text-anchor="middle">Login</text>
    <rect x="692" y="779" width="19" height="19" fill="none" stroke="#fff" stroke-width=".8"/>
    <path d="M698 785h7M698 788.5h7M698 792h7" stroke="#fff" stroke-width="1"/>
    <text x="625" y="822" font-size="18" font-weight="600" fill="#fff" text-anchor="middle" font-family="Montserrat, sans-serif">Swift Tee</text>
    <text x="544" y="862" font-size="10" fill="#fff">Welcome to Swift Tee.</text>
    <path d="M544 865h122" stroke="#fff" stroke-width=".6"/>
    <text x="544" y="880" font-size="6.5" fill="#fff">You can pay your Swift Tee fees for participating</text>
    <text x="544" y="890" font-size="6.5" fill="#fff">clubs here.</text>
    <text x="544" y="913" font-size="10" fill="#fff">Choose your Club</text>
    <rect x="544" y="928" width="158" height="18" fill="#fff"/>
    <circle cx="569" cy="936" r="2.6" fill="none" stroke="#99a" stroke-width=".8"/>
    <text x="580" y="939.5" font-size="6.5" fill="#99a">Type the Name of your Club</text>
    <text x="544" y="974" font-size="9.5" fill="#fff">How many Players and Holes</text>
    <rect x="544" y="989" width="47" height="16" fill="none" stroke="#fff" stroke-width=".9"/>
    <path d="M567.5 989v16M551 997h9M575 997h9M579.5 992.5v9" stroke="#fff" stroke-width="1"/>
    <rect x="597" y="989" width="29" height="16" fill="#fff"/>
    <text x="611.5" y="1000" font-size="6.5" fill="#333" text-anchor="middle">4</text>
    <text x="655" y="1000" font-size="6" fill="#fff">9</text>
    <rect x="663" y="989" width="25" height="15" rx="7.5" fill="#fff"/>
    <circle cx="671" cy="996.5" r="6.5" fill="#e8e8e8" stroke="#ccc" stroke-width=".6"/>
    <text x="693" y="1000" font-size="6" fill="#fff">18</text>
    <text x="544" y="1029" font-size="10" fill="#fff">Greens Total:  $15.00</text>
    <rect x="544" y="1045" width="158" height="24" fill="var(--button-grey)"/>
    <text x="623" y="1060.5" font-size="8" fill="#fff" text-anchor="middle">Submit</text>
    <g fill="#cfdedd"><circle cx="611" cy="1080" r="1.3"/><circle cx="619" cy="1080" r="1.3"/><circle cx="627" cy="1080" r="1.3"/><circle cx="635" cy="1080" r="1.3"/></g>
  </svg>
</main>
</body>
</html>
```